sailbrightly Website for children with diabilities

Hi, we are looking for a new website design for our community service "sailbrightly". Sailbrightly gives children who suffer from diseases or disabilities a week off on a Boat to give the children new hope and an unforgettable experience.

The current website is really old and we want to have a new one.
Please feel free to discover our website under http://sailbrightly-example.at/.
We have several company sponsors which are very important to us.

The Website has to be a Bootstrap Design (Version 4.4 or higher) [NOT Wordpress, Joomla, other CMS]

Target Market(s)

no target market. we like to inform our communities about our service.

Industry/Entity Type

community service for children with disabilities

Coding

Number of Pages Required

4 page

Font styles to use
Sans Serif

Colors
0054AA
0677BA
7BADD7
CADEEF
E8F1F8
0094D4
00A9DD
6FCCEA
C7EBF8
E9F6FB

Requirements
Must have
• About, Sponsors, Information about cruises
Nice to have
• Gallery

```html
<!DOCTYPE html>
<html lang="en">
<head>
<meta charset="utf-8">
<title>Sailbrightly</title>
<link rel="stylesheet" href="https://fonts.googleapis.com/css2?family=Roboto:wght@400;500;700;900&family=Ubuntu:wght@400;500&display=swap">
<style>
:root{
  --navy:#1b1f6b;
  --navy-deep:#151a5c;
  --ink:#1a1a1a;
  --text:#2b2b2b;
  --white:#ffffff;
  --light:#f4f6fb;
  --line:#e3e6ee;
  --sea:#3d8fc4;
  --sky:#7bb4dc;
  --sand:#e9dfd0;
}
*{box-sizing:border-box;margin:0;padding:0}
html,body{width:1200px;height:3997px;overflow:hidden;background:var(--white);font-family:'Roboto',sans-serif;color:var(--text)}
.page{position:relative;width:1200px;height:3997px;overflow:hidden}
.abs{position:absolute}
.photo{position:absolute}
.btn{position:absolute;display:flex;align-items:center;justify-content:center;background:var(--navy);color:var(--white);font-weight:700;font-size:13px;letter-spacing:.2px;border-radius:22px;text-transform:uppercase}
.btn--outline{border:2px solid var(--white)}

/* hero */
.hero{position:absolute;left:0;top:0;width:1200px;height:700px;background:linear-gradient(180deg,#4d7fc0 0%,#6fa4d4 16%,#3c9ac7 24%,#2d87b6 40%,#7fb7cf 55%,#cfd9d9 72%,#e6dfd2 100%)}
.hero__wave{position:absolute;left:0;top:600px}
.brand{position:absolute;left:104px;top:6px;display:flex;align-items:center;gap:14px}
.brand__mark{width:106px;height:106px;border-radius:50%;background:var(--white);border:4px solid var(--navy)}
.brand__name{font-family:'Ubuntu',sans-serif;font-size:22px;color:var(--white);font-weight:500}
.nav{position:absolute;top:52px;left:517px;display:flex;gap:0;font-size:14px;color:var(--white)}
.nav a{color:var(--white);text-decoration:none;position:absolute;white-space:nowrap}
.hero__title{position:absolute;left:659px;top:218px;color:var(--white);font-weight:700;line-height:1}
.hero__title .small{font-size:52px;display:block}
.hero__title .big{font-size:76px;display:block;margin-top:22px}

/* about */
.about__ring{position:absolute;left:102px;top:825px;width:526px;height:526px;border-radius:50%;border:2px solid var(--navy)}
.about__photo{position:absolute;left:108px;top:831px;width:514px;height:514px;border-radius:50%;background:radial-gradient(circle at 50% 28%,#f6e0c4 0%,#e9b98d 30%,#8f8a92 60%,#4b4a55 100%)}
.h2{position:absolute;font-weight:700;color:var(--ink);font-size:56px;line-height:1}
.about__text{position:absolute;left:677px;top:936px;width:424px;font-size:13.6px;line-height:20.7px;color:var(--text)}

/* cruises */
.band{position:absolute;left:0;top:1410px;width:1200px;height:480px;background:var(--navy)}
.card{position:absolute;top:1623px;width:316px;height:457px;background:var(--white);box-shadow:0 4px 14px rgba(0,0,0,.12)}
.card__img{height:267px}
.card__title{margin-top:22px;text-align:center;font-weight:700;font-size:18px;color:var(--ink)}
.card__text{margin:10px auto 0;width:270px;text-align:center;font-size:11px;line-height:16px;color:var(--text)}
.card__price{margin-top:10px;text-align:center;font-weight:700;font-size:14px;color:var(--ink)}
.card .btn{position:relative;margin:12px auto 0;width:136px;height:30px;font-size:12px}
.arrow{position:absolute}

/* gallery */
/* sponsors */
.sponsors{position:absolute;left:0;top:3050px;width:1200px;height:560px;background:var(--light)}
.logo{position:absolute;width:238px;height:111px;background:var(--white);border:2px solid var(--line);display:flex;align-items:center;justify-content:center;font-size:26px;font-weight:700;color:var(--navy)}

/* footer */
.footer{position:absolute;left:0;top:3530px}
.footer__col{position:absolute;color:var(--white)}
.footer__head{font-size:21px;font-weight:500}
.footer__list{list-style:none;margin-top:17px;font-size:14px}
.footer__list li{height:30px;display:flex;align-items:center;gap:11px}
.footer__rule{position:absolute;left:0;top:3923px;width:1200px;height:1px;background:rgba(255,255,255,.35)}
.copyright{position:absolute;left:0;top:3946px;width:1200px;text-align:center;color:var(--white);font-size:14px}
</style>
</head>
<body>
<div class="page">

  <!-- hero -->
  <section class="hero">
    <div class="photo" role="img" aria-label="Photo of a man and a boy in a wheelchair sitting together on a beach facing the sea" style="left:0;top:0;width:1200px;height:700px;background:radial-gradient(ellipse 260px 300px at 360px 470px,rgba(40,50,110,.55),rgba(40,50,110,0) 70%)"></div>
    <svg class="hero__wave" width="1200" height="100" viewBox="0 0 1200 100"><path d="M0 40 C150 90 300 90 520 60 C760 28 950 20 1200 55 L1200 100 L0 100 Z" fill="#fff"/></svg>
  </section>

  <header>
    <div class="brand">
      <div class="brand__mark"></div>
      <span class="brand__name">Verein Sailbrightly</span>
    </div>
    <nav class="nav">
      <a style="left:0;font-weight:700">HOME</a>
      <a style="left:82px">ABOUT</a>
      <a style="left:165px">SPONSORS</a>
      <a style="left:283px">CRUISES</a>
      <a style="left:377px">GALLERY</a>
    </nav>
    <div class="btn btn--outline" style="left:986px;top:42px;width:136px;height:42px">Donate Now</div>
  </header>

  <div class="hero__title">
    <span class="small">Welcome to</span>
    <span class="big">Sailbrightly</span>
  </div>
  <div class="btn btn--outline" style="left:659px;top:387px;width:168px;height:40px">Donate Now</div>

  <!-- about -->
  <div class="about__ring"></div>
  <div class="about__photo" role="img" aria-label="Photo of a boy in a wheelchair on a beach at sunset"></div>
  <h2 class="h2" style="left:683px;top:858px">About Us</h2>
  <p class="about__text">Trained social workers and experienced skippers who volunteer in the Sailbrightly association and organize a fleet every year for socially disadvantaged children and young people from central Upper Austria and set up the necessary financial resources.enabling children and young people who don't always have it easy in life to spend an unforgettable week in Croatia. It is precisely this shared experience that gives the children and young people a new zest for life and perspectives for their future. Through the reflection and also the care afterwards in the individual facilities, the children and young people can draw on this experience for a long time to come. This sustainability creates numerous pedagogical points of contact that represent a valuable basis for the achievement of goals.</p>
  <div class="btn" style="left:677px;top:1232px;width:137px;height:39px">Read More</div>

  <!-- cruises -->
  <section class="band"></section>
  <h2 class="h2" style="left:0;top:1522px;width:1200px;text-align:center;color:#fff">About Cruises</h2>

  <article class="card" style="left:99px">
    <div class="card__img" role="img" aria-label="Photo of a white cruise ship on blue sea" style="background:linear-gradient(180deg,#6aa6d6 0%,#9cc6e6 45%,#2f78b4 60%,#1d5d97 100%)"></div>
    <div class="card__title">Lorem ipsum dolor sit amet</div>
    <div class="card__text">Lorem ipsum dolor sit amet, consectetur adipiscing elit, sed do eiusmod tempor incididunt aliqua.</div>
    <div class="card__price">$ 25.00</div>
    <div class="btn">Enquairy Now</div>
  </article>
  <article class="card" style="left:443px">
    <div class="card__img" role="img" aria-label="Photo of a cruise ship at sunset" style="background:linear-gradient(180deg,#30518a 0%,#c98b6a 45%,#e2a36f 55%,#2c3f63 75%,#1d2b49 100%)"></div>
    <div class="card__title">Lorem ipsum dolor sit amet</div>
    <div class="card__text">Lorem ipsum dolor sit amet, consectetur adipiscing elit, sed do eiusmod tempor incididunt aliqua.</div>
    <div class="card__price">$ 25.00</div>
    <div class="btn">Enquairy Now</div>
  </article>
  <article class="card" style="left:786px">
    <div class="card__img" role="img" aria-label="Photo of a boy looking over a ship railing" style="background:linear-gradient(90deg,#f2f4f6 0%,#dfe4ea 45%,#8fb4d0 70%,#5d7f9c 100%)"></div>
    <div class="card__title">Lorem ipsum dolor sit amet</div>
    <div class="card__text">Lorem ipsum dolor sit amet, consectetur adipiscing elit, sed do eiusmod tempor incididunt aliqua.</div>
    <div class="card__price">$ 25.00</div>
    <div class="btn">Enquairy Now</div>
  </article>

  <svg class="arrow" style="left:26px;top:1720px" width="48" height="48" viewBox="0 0 48 48"><circle cx="24" cy="24" r="22" fill="none" stroke="#fff" stroke-width="2"/><path d="M27 15 L18 24 L27 33" fill="none" stroke="#fff" stroke-width="2"/></svg>
  <svg class="arrow" style="left:1126px;top:1720px" width="48" height="48" viewBox="0 0 48 48"><circle cx="24" cy="24" r="22" fill="none" stroke="#fff" stroke-width="2"/><path d="M21 15 L30 24 L21 33" fill="none" stroke="#fff" stroke-width="2"/></svg>

  <!-- gallery -->
  <h2 class="h2" style="left:0;top:2160px;width:1200px;text-align:center">Gallery</h2>
  <div class="photo" role="img" aria-label="Photo of a mother and child watching a harbour with container ships" style="left:99px;top:2282px;width:407px;height:302px;background:linear-gradient(180deg,#b5523f 0%,#8a6b63 20%,#6e7c8a 45%,#c9b79a 70%,#d9dde4 100%)"></div>
  <div class="photo" role="img" aria-label="Photo of a smiling girl on a boat deck in a city harbour" style="left:530px;top:2282px;width:312px;height:302px;background:linear-gradient(180deg,#3a8fd6 0%,#8ec1e8 35%,#e3d49d 65%,#2f6ea3 100%)"></div>
  <div class="photo" role="img" aria-label="Photo of a boy giving a thumbs up on a ship" style="left:867px;top:2284px;width:233px;height:300px;background:linear-gradient(135deg,#e9ecef 0%,#d9c3a6 40%,#a7c7e0 80%,#6c93b8 100%)"></div>
  <div class="photo" role="img" aria-label="Photo of a smiling girl in a red jacket leaning on a stone wall" style="left:99px;top:2610px;width:569px;height:276px;background:linear-gradient(180deg,#7f8a8d 0%,#a2a6a3 40%,#c34150 65%,#8e8d86 100%)"></div>
  <div class="photo" role="img" aria-label="Photo of children and adults on a sailing boat" style="left:690px;top:2610px;width:410px;height:274px;background:linear-gradient(180deg,#d7e6f2 0%,#9bc2df 35%,#e9d6c8 65%,#3f87b8 100%)"></div>
  <div class="btn" style="left:541px;top:2930px;width:118px;height:40px">View More</div>

  <!-- sponsors -->
  <section class="sponsors"></section>
  <h2 class="h2" style="left:0;top:3113px;width:1200px;text-align:center">Sponsors</h2>
  <div class="logo" style="left:99px;top:3198px">Kornfeld</div>
  <div class="logo" style="left:352px;top:3198px">Talvero</div>
  <div class="logo" style="left:606px;top:3198px">M. Brandtner</div>
  <div class="logo" style="left:860px;top:3198px">Ostwald</div>
  <div class="logo" style="left:99px;top:3337px">baerenmut</div>
  <div class="logo" style="left:352px;top:3337px">Lindhof</div>
  <div class="logo" style="left:606px;top:3337px">SV Bergtal</div>
  <div class="logo" style="left:860px;top:3337px">Moser</div>
  <svg class="arrow" style="left:26px;top:3306px" width="48" height="48" viewBox="0 0 48 48"><circle cx="24" cy="24" r="22" fill="none" stroke="#1a1a1a" stroke-width="2"/><path d="M27 15 L18 24 L27 33" fill="none" stroke="#1a1a1a" stroke-width="2"/></svg>
  <svg class="arrow" style="left:1126px;top:3306px" width="48" height="48" viewBox="0 0 48 48"><circle cx="24" cy="24" r="22" fill="none" stroke="#1a1a1a" stroke-width="2"/><path d="M21 15 L30 24 L21 33" fill="none" stroke="#1a1a1a" stroke-width="2"/></svg>

  <!-- footer -->
  <svg class="footer" width="1200" height="467" viewBox="0 0 1200 467"><path d="M0 40 C200 80 380 65 620 40 C850 15 1030 10 1200 20 L1200 467 L0 467 Z" fill="var(--navy)"/></svg>
  <div class="footer__col" style="left:103px;top:3658px">
    <div class="footer__head" style="font-family:'Ubuntu',sans-serif;font-weight:400">Verein Sailbrightly</div>
    <div style="margin:22px 0 0 58px;width:108px;height:108px;border-radius:50%;background:#fff;border:4px solid var(--navy-deep)"></div>
  </div>
  <div class="footer__col" style="left:453px;top:3657px">
    <div class="footer__head">Navigation</div>
    <ul class="footer__list">
      <li>Home</li><li>About</li><li>Sponsors</li><li>Info About Cruises</li><li>Gallery</li>
    </ul>
  </div>
  <div class="footer__col" style="left:678px;top:3657px">
    <div class="footer__head">Project Goals</div>
    <ul class="footer__list">
      <li><svg width="15" height="15" viewBox="0 0 16 16"><circle cx="8" cy="8" r="7" fill="none" stroke="#fff"/><path d="M6.5 4.5 L10 8 L6.5 11.5" fill="none" stroke="#fff"/></svg>Strengthening of self-esteem and social skills</li>
      <li><svg width="15" height="15" viewBox="0 0 16 16"><circle cx="8" cy="8" r="7" fill="none" stroke="#fff"/><path d="M6.5 4.5 L10 8 L6.5 11.5" fill="none" stroke="#fff"/></svg>Take responsibility for yourself and others</li>
      <li><svg width="15" height="15" viewBox="0 0 16 16"><circle cx="8" cy="8" r="7" fill="none" stroke="#fff"/><path d="M6.5 4.5 L10 8 L6.5 11.5" fill="none" stroke="#fff"/></svg>practicing tolerance</li>
      <li><svg width="15" height="15" viewBox="0 0 16 16"><circle cx="8" cy="8" r="7" fill="none" stroke="#fff"/><path d="M6.5 4.5 L10 8 L6.5 11.5" fill="none" stroke="#fff"/></svg>Development of non-violent conflict resolution strategies</li>
      <li><svg width="15" height="15" viewBox="0 0 16 16"><circle cx="8" cy="8" r="7" fill="none" stroke="#fff"/><path d="M6.5 4.5 L10 8 L6.5 11.5" fill="none" stroke="#fff"/></svg>Experiential Learning</li>
    </ul>
  </div>
  <div class="footer__rule"></div>
  <div class="copyright">2022 © Sailbrightly. All Rights are reserved.</div>

</div>
</body>
</html>
```